Wellness Wordpress Blog Redesign

I am looking to redesign by wordpress blog - www.MarenCrowleyActive.com. I would like to have a more personalized feel that resonates with my brand of Renewed Balance through fitness, nutrition, self care and self love. I'd like capabilities to do the following:

Ideally, I'd like to have the home page feature not only my latest blog posts or videos, but to also include a place to click to learn more about other facets of my business.

Ideally, I'd love to have a page layout of:

Home - main page to host key features of the brand & latest blog posts
About - Place to learn more about me and my brand
Blog -
Fitness - Host some videos and fitness tips and links to resources
Nutrition - Host some videos and recipes and links to resources
Self Care - Host some videos and self care tips and links to resources
Shop - Host a video (that can be changed of the product of the month) and links to other resources

Number of Pages Required

5+ page

Font styles to use
Serif
Decorative

Colors
85acd3
0393ce
00a990
6b449b
a64599
b8a6cd

Requirements
Must have
• Home - main page to host key features of the brand & latest blog posts
• About - Place to learn more about me and my brand
• Blog -
• Fitness - Host some videos and fitness tips and links to resources
• Nutrition - Host some videos and recipes and links to resources
• Self Care - Host some videos and self care tips and links to resources
• Shop - Host a video (that can be changed of the product of the month) and links to other resources
• Video / Mutlimedia capabilities
Nice to have
• Option to have a calendar of events widgets for people to sign up for events that I'm hosting

```html
<!DOCTYPE html>
<html lang="en">
<head>
<meta charset="utf-8">
<title>Maren Crowley — Training &amp; Coaching</title>
<link href="https://fonts.googleapis.com/css2?family=Raleway:wght@400;500;600&family=Open+Sans:wght@400;600&display=swap" rel="stylesheet">
<style>
:root{
  --teal:#13a89e;
  --teal-light:#1fc7b3;
  --teal-dark:#0c9486;
  --purple:#6b2f8a;
  --purple-light:#a64599;
  --ink:#333333;
  --muted:#777777;
  --grey-band:#efefef;
  --line:#dddddd;
  --footer:#2b2b2b;
  --footer-deep:#1e1e1e;
  --white:#ffffff;
}
*{box-sizing:border-box;margin:0;padding:0}
html,body{width:1200px;height:3871px;overflow:hidden}
body{position:relative;background:var(--white);font-family:"Open Sans",Arial,sans-serif;color:var(--ink)}
.abs{position:absolute}
.heading{font-family:"Raleway",Arial,sans-serif;font-weight:500}
.btn{position:absolute;background:var(--teal);color:var(--white);border-radius:22px;font-size:14px;font-weight:600;display:flex;align-items:center;justify-content:center}

/* header */
.top-rule{left:0;top:0;width:1200px;height:8px;background:var(--teal)}
.brand{left:98px;top:70px;display:flex;flex-direction:column;align-items:center;width:310px}
.brand-name{font-family:"Raleway",Arial,sans-serif;font-weight:600;font-size:44px;color:var(--purple);letter-spacing:1px}
.brand-tag{font-family:"Raleway",Arial,sans-serif;font-weight:600;font-size:13px;color:var(--purple);letter-spacing:4px;margin-top:2px}
.main-nav{right:60px;top:98px;display:flex;font-size:14px;color:var(--ink)}
.main-nav span{padding:0 10px;border-left:1px solid #999}
.main-nav span:first-child{border-left:none}

/* hero */
.hero{left:0;top:206px;width:1200px;height:599px;background:linear-gradient(100deg,#d7dff0 0%,#c9d3ec 35%,#b8c4e0 60%,#dfe3ee 100%)}
.hero-title{left:98px;top:390px;font-size:38px;line-height:47px;color:#222;font-family:"Raleway",Arial,sans-serif}
.hero-arrow{width:40px;height:40px;border-radius:50%;background:rgba(90,90,90,.7);top:466px}

/* about */
.about{left:0;top:805px;width:1200px;height:459px;background:var(--grey-band)}
.about-photo{left:98px;top:857px;width:431px;height:345px;border:4px solid #fff;outline:1px solid var(--line);background:linear-gradient(135deg,#5f7a3a,#8aa25a 50%,#4b5d2c)}
.about-title{left:586px;top:862px;font-size:32px;color:var(--purple)}
.about-text{left:586px;top:912px;width:520px;font-size:12.5px;line-height:22.5px;color:#444}

/* services */
.section-title{width:1200px;left:0;text-align:center;font-size:34px;color:var(--purple)}
.service{width:212px;height:212px;border-radius:50%;top:1403px;display:flex;flex-direction:column;align-items:center;justify-content:flex-end;padding-bottom:48px;color:#fff;font-family:"Raleway",Arial,sans-serif;font-weight:600;font-size:19px;line-height:24px;text-align:center;box-shadow:0 4px 8px rgba(0,0,0,.15)}
.service svg{margin-bottom:14px}
.service.teal{background:radial-gradient(circle at 50% 30%,var(--teal-light),var(--teal-dark))}
.service.purple{background:radial-gradient(circle at 50% 30%,#b95bb8,var(--purple))}

/* news + video */
.band{left:0;top:1811px;width:1200px;height:454px;background:var(--grey-band)}
.col-title{top:1852px;font-size:32px;color:var(--purple)}
.news-item{left:98px;width:480px;display:flex;gap:22px}
.news-thumb{width:72px;height:62px;flex:none}
.news-date{color:var(--teal);font-weight:600;font-size:14px;margin:6px 0 6px}
.news-date svg{vertical-align:-2px;margin-right:6px}
.news-copy{font-size:11px;line-height:15px;color:#666}
.news-rule{left:200px;width:310px;height:1px;background:#ccc}
.video{left:640px;top:1922px;width:459px;height:240px;background:linear-gradient(180deg,#3c4a58,#24303a 60%,#141a20)}

/* blog */
.card{left:98px;width:1001px;height:317px;background:#fff;border:1px solid var(--line);box-shadow:0 2px 6px rgba(0,0,0,.06)}
.card-title{font-family:"Raleway",Arial,sans-serif;font-weight:500;font-size:20px;line-height:29px;color:#222;width:410px}
.card-body{font-size:12px;line-height:22px;color:#777;width:410px;margin-top:16px}
.card-meta{font-size:12px;color:#777;margin-top:26px}
.card-photo{width:369px;height:243px}

/* footer */
.footer{left:0;top:3514px;width:1200px;height:317px;background:var(--footer)}
.footer-base{left:0;top:3831px;width:1200px;height:40px;background:var(--footer-deep);color:#aaa;font-size:12px;padding:12px 98px}
.f-head{top:3568px;color:#fff;font-family:"Raleway",Arial,sans-serif;font-weight:600;font-size:15px}
.field{background:#fff;border:1px solid #bbb;font-size:11px;color:#555;padding:5px 8px}
.f-links{left:482px;top:3615px;color:#fff;font-size:11px;line-height:31px}
.social{width:24px;height:24px;border-radius:50%}
.contact-line{left:906px;color:#fff;font-size:12px;display:flex;gap:14px;align-items:center}
</style>
</head>
<body>

<header>
  <div class="abs top-rule"></div>
  <div class="abs brand">
    <span class="brand-name">Maren Crowley</span>
    <span class="brand-tag">TRAINING &amp; COACHING</span>
  </div>
  <nav class="abs main-nav">
    <span>HOME</span><span>ABOUT</span><span>BLOG</span><span>FITNESS</span><span>NUTRITIONS</span><span>SELF CARES</span><span>SHOP</span><span>VIDEO</span>
  </nav>
</header>

<section>
  <div class="abs hero" role="img" aria-label="Woman in workout clothes stretching on a floor beside an exercise ball in a bright studio"></div>
  <h1 class="abs hero-title" style="font-weight:400">Bodyweight Training<br>For Men &amp; Women..</h1>
  <div class="btn" style="left:98px;top:514px;width:148px;height:42px">Contact Now</div>
  <div class="abs hero-arrow" style="left:12px"><svg width="40" height="40"><path d="M23 13 L16 20 L23 27" fill="none" stroke="#fff" stroke-width="3"/></svg></div>
  <div class="abs hero-arrow" style="right:0"><svg width="40" height="40"><path d="M17 13 L24 20 L17 27" fill="none" stroke="#fff" stroke-width="3"/></svg></div>
</section>

<section>
  <div class="abs about"></div>
  <div class="abs about-photo" role="img" aria-label="Woman in a pink top doing a lunge on a forest path"></div>
  <h2 class="abs heading about-title">About Me</h2>
  <p class="abs about-text">Lorem Ipsum is simply dummy text of the printing and typesetting industry.<br>Lorem Ipsum has been the industry's standard dummy text ever since the 1500s, when an unknown printer took a galley of type and scrambled it to make a type specimen book.<br>It has survived not only five centuries, but also the leap into electronic typesetting, remaining essentially unchanged. It was popularised in the 1960s with the release of Letraset sheets containing Lorem Ipsum passages,<br>and more recently with desktop publishing software like Aldus PageMaker including versions of Lorem Ipsum.<br>It is a long established fact that a reader will be distracted by the readable content of a page when looking at its layout. The point of using Lorem Ipsum is that it has a more-or-less normal distribution of letters, as opposed to using 'Content here, content here', making it look like readable English.</p>
</section>

<section>
  <h2 class="abs heading section-title" style="top:1300px">My Services</h2>
  <div class="abs service teal" style="left:100px">
    <svg width="50" height="60" viewBox="0 0 50 60"><circle cx="28" cy="8" r="6" fill="#fff"/><path d="M24 16 L18 34 L8 56 M20 30 L32 40 L36 58 M22 20 L38 26 M24 18 L10 24" stroke="#fff" stroke-width="6" fill="none" stroke-linecap="round"/></svg>
    <span>Fitness<br>Assessment</span>
  </div>
  <div class="abs service purple" style="left:371px">
    <svg width="70" height="56" viewBox="0 0 70 56"><circle cx="30" cy="10" r="7" fill="#fff"/><path d="M30 20 L40 38 L62 44 M34 28 L12 44 M8 52 H64" stroke="#fff" stroke-width="6" fill="none" stroke-linecap="round"/></svg>
    <span>Warm Up, Stretching<br>&amp; Cool Down</span>
  </div>
  <div class="abs service teal" style="left:616px">
    <svg width="90" height="40" viewBox="0 0 90 40"><rect x="6" y="8" width="10" height="24" rx="2" fill="#fff"/><rect x="18" y="2" width="10" height="36" rx="2" fill="#fff"/><rect x="62" y="2" width="10" height="36" rx="2" fill="#fff"/><rect x="74" y="8" width="10" height="24" rx="2" fill="#fff"/><rect x="28" y="16" width="34" height="8" fill="#fff"/></svg>
    <span>Free Weight Training<br>&amp; Instruction</span>
  </div>
  <div class="abs service purple" style="left:887px">
    <svg width="60" height="56" viewBox="0 0 60 56"><circle cx="18" cy="36" r="16" fill="#fff"/><path d="M18 20 Q20 12 26 10" stroke="#fff" stroke-width="3" fill="none"/><rect x="36" y="14" width="20" height="40" rx="3" fill="#fff"/><rect x="38" y="4" width="16" height="8" fill="#fff"/></svg>
    <span>Nutrition<br>Plans</span>
  </div>
  <div class="btn" style="left:526px;top:1710px;width:145px;height:42px">Contact Now</div>
</section>

<section>
  <div class="abs band"></div>
  <h2 class="abs heading col-title" style="left:98px">News &amp; Events</h2>
  <h2 class="abs heading col-title" style="left:640px">Watch Video</h2>

  <div class="abs news-item" style="top:1922px">
    <div class="news-thumb" role="img" aria-label="Note card with a handwritten reminder" style="background:linear-gradient(135deg,#d9d4c8,#9a8f7c)"></div>
    <div><p class="news-date"><svg width="14" height="14"><rect x="1" y="2" width="12" height="11" fill="none" stroke="#13a89e" stroke-width="1.6"/><path d="M1 5 H13" stroke="#13a89e" stroke-width="1.6"/></svg>Jul 06, 2018</p>
    <p class="news-copy">Sed ut perspiciatis unde omnis iste natus error sit, voluptatem doloremque laudantium, totam rem.</p></div>
  </div>
  <div class="abs news-rule" style="top:2010px"></div>
  <div class="abs news-item" style="top:2033px">
    <div class="news-thumb" role="img" aria-label="Two people smiling at an event" style="background:linear-gradient(135deg,#c8b6a4,#6f5a48)"></div>
    <div><p class="news-date"><svg width="14" height="14"><rect x="1" y="2" width="12" height="11" fill="none" stroke="#13a89e" stroke-width="1.6"/><path d="M1 5 H13" stroke="#13a89e" stroke-width="1.6"/></svg>Jun 25, 2018</p>
    <p class="news-copy">Nemo enim ipsam voluptatem quia voluptas sit aspernatur aut odit fugit, sed quia magni.</p></div>
  </div>
  <div class="abs news-rule" style="top:2123px"></div>
  <div class="abs news-item" style="top:2147px">
    <div class="news-thumb" role="img" aria-label="Couple standing together outdoors" style="background:linear-gradient(135deg,#e4d8cc,#a88c74)"></div>
    <div><p class="news-date"><svg width="14" height="14"><rect x="1" y="2" width="12" height="11" fill="none" stroke="#13a89e" stroke-width="1.6"/><path d="M1 5 H13" stroke="#13a89e" stroke-width="1.6"/></svg>Jun 09, 2018</p>
    <p class="news-copy">Neque porro quisquam est qui dolorem ipsum quia dolor sit amet, consectetur velit sed.</p></div>
  </div>

  <div class="abs video" role="img" aria-label="Video still of a woman in sportswear on a beach at dusk"></div>
  <svg class="abs" style="left:846px;top:2018px" width="46" height="46"><circle cx="23" cy="23" r="20" fill="none" stroke="#fff" stroke-width="3"/><path d="M18 14 L32 23 L18 32 Z" fill="#fff"/></svg>
  <svg class="abs" style="left:640px;top:2132px" width="459" height="30"><rect width="459" height="30" fill="rgba(0,0,0,.55)"/><path d="M14 9 L24 15 L14 21 Z" fill="#fff"/><rect x="64" y="14" width="300" height="3" fill="#888"/><rect x="380" y="14" width="30" height="3" fill="#ccc"/><rect x="425" y="9" width="14" height="12" fill="none" stroke="#fff" stroke-width="2"/></svg>
</section>

<section>
  <h2 class="abs heading section-title" style="top:2316px">Blog</h2>

  <article class="abs card" style="top:2392px">
    <div class="abs" style="left:57px;top:32px">
      <h3 class="card-title">Lorem Ipsum is simply dummy text of the printing and typesetting industry.</h3>
      <p class="card-body">Lorem Ipsum is simply dummy text of the printing and typesetting industry. Lorem Ipsum has been the industry's standard dummy text ever since the 1500s, when an unknown printer took a galley of type and scrambled it to make a type specimen book.<br>It has survived not only five centuries, but also the leap into electronic typesetting, remaining essentially unchanged.</p>
      <p class="card-meta">Sep 30, 2017 &nbsp;|&nbsp; by admin</p>
    </div>
    <div class="abs card-photo" style="left:573px;top:33px;background:linear-gradient(135deg,#c9a88c,#e8d8c8 60%,#b8a08a)" role="img" aria-label="Smiling woman resting her head on her hand"></div>
  </article>

  <article class="abs card" style="top:2758px">
    <div class="abs card-photo" style="left:62px;top:33px;background:linear-gradient(135deg,#b89272,#d8c0a0 55%,#6e5a48)" role="img" aria-label="Two women doing plank exercises in a gym"></div>
    <div class="abs" style="left:521px;top:32px">
      <h3 class="card-title">Lorem Ipsum is simply dummy text of the printing and typesetting industry.</h3>
      <p class="card-body">Lorem Ipsum is simply dummy text of the printing and typesetting industry. Lorem Ipsum has been the industry's standard dummy text ever since the 1500s, when an unknown printer took a galley of type and scrambled it to make a type specimen book.<br>It has survived not only five centuries, but also the leap into electronic typesetting, remaining essentially unchanged.</p>
      <p class="card-meta">Sep 30, 2017 &nbsp;|&nbsp; by admin</p>
    </div>
  </article>

  <article class="abs card" style="top:3124px">
    <div class="abs" style="left:57px;top:32px">
      <h3 class="card-title">Lorem Ipsum is simply dummy text of the printing and typesetting industry.</h3>
      <p class="card-body">Lorem Ipsum is simply dummy text of the printing and typesetting industry. Lorem Ipsum has been the industry's standard dummy text ever since the 1500s, when an unknown printer took a galley of type and scrambled it to make a type specimen book.<br>It has survived not only five centuries, but also the leap into electronic typesetting, remaining essentially unchanged.</p>
      <p class="card-meta">Sep 30, 2017 &nbsp;|&nbsp; by admin</p>
    </div>
    <div class="abs card-photo" style="left:573px;top:33px;background:linear-gradient(135deg,#4a3626,#7aa05a 45%,#c8a070 75%,#3a2a1e)" role="img" aria-label="Bowl of salad with avocado, grains and chicken on a wooden table"></div>
  </article>
</section>

<footer>
  <div class="abs footer"></div>
  <h4 class="abs f-head" style="left:98px">SEND MESSAGE</h4>
  <div class="abs field" style="left:98px;top:3620px;width:140px;height:25px">NAME</div>
  <div class="abs field" style="left:246px;top:3620px;width:141px;height:25px">EMAIL</div>
  <div class="abs field" style="left:98px;top:3652px;width:289px;height:78px">MESSAGE</div>
  <div class="btn" style="left:279px;top:3738px;width:108px;height:31px;font-size:11px">Send Message</div>

  <h4 class="abs f-head" style="left:482px">SITE LINKS</h4>
  <div class="abs f-links">ABOUT ME<br>MY SERVICES<br>EVENTS<br>BLOG<br>CONTACT ME</div>

  <h4 class="abs f-head" style="left:699px">FOLLOW US</h4>
  <div class="abs social" style="left:699px;top:3610px;background:#3b5a9a"></div>
  <div class="abs social" style="left:729px;top:3610px;background:#29a8e0"></div>
  <div class="abs social" style="left:759px;top:3610px;background:#8a6a50"></div>
  <div class="abs social" style="left:699px;top:3645px;background:#d82a2a"></div>
  <div class="abs social" style="left:729px;top:3645px;background:#d84a3a"></div>
  <div class="abs social" style="left:759px;top:3645px;background:#1f7ab8"></div>

  <h4 class="abs f-head" style="left:906px">CONTACT US</h4>
  <div class="abs contact-line" style="top:3614px"><svg width="12" height="16" viewBox="0 0 12 16"><path d="M6 0 C2.7 0 0 2.6 0 6 C0 10 6 16 6 16 S12 10 12 6 C12 2.6 9.3 0 6 0 Z" fill="#bbb"/><circle cx="6" cy="6" r="2.3" fill="#2b2b2b"/></svg>National Institute of Movement Coaching</div>
  <div class="abs contact-line" style="top:3664px"><svg width="15" height="11"><rect x=".5" y=".5" width="14" height="10" fill="none" stroke="#bbb"/><path d="M1 1 L7.5 6 L14 1" fill="none" stroke="#bbb"/></svg>maren@marencrowleyactive.com</div>
  <div class="abs" style="left:893px;top:3722px;width:217px;text-align:center">
    <div style="font-family:'Raleway',sans-serif;font-weight:600;font-size:30px;color:#fff">Maren Crowley</div>
    <div style="font-family:'Raleway',sans-serif;font-weight:600;font-size:9px;color:#fff;letter-spacing:3px">TRAINING &amp; COACHING</div>
  </div>
  <div class="abs footer-base">Copyright © 2018 marencrowleyactive.com All rights reserved.</div>
</footer>

</body>
</html>
```